Home and interior page website design for HVAC company - Velmor Corp.

Create homepage and one interior page website design for an HVAC (Heating and AC) company. Current website is: https://velmorcorp.example/.

Client has specifically asked that the new site look inviting, informative and interactive. They mentioned that the logo on a white background doesn't look appealing and would like to see other options. (I have included the white background one from their current website as well as the one on an image that the client sent me) The site must include their financing widget (we have the code for this) in a prominent place. Image can be found here: https://getlendquick.example/badges/lendquick-financing.png.

The content from their existing site belongs to the company that built their site and have said we cannot use any of it. This development site (http://velmorwebd.qrbdev.example/) is what we originally created from our template for them before they decided they wanted a custom built site. The content there is what will need to be on the new home page.

We have gathered images from the client that they would like used throughout the site in this folder: https://climbrisk-my.filebox.example/:f:/g/personal/officelogin_climbrisk_filebox_example/Xq2m-R7TpLoWnZbYuCdE5FgHjK8NvA3sQwErTyUiOpLk?e=7KPZRT. They would like the photos used to be in tune with the topic being spoken about so if the topic is maintenance on a central AC system the photo used to lead that topic should be of a unit being cleaned.

For the testimonials section please also include a button or "Click here for more testimonials" as requested by the client.

Top Level NAV should include: Home, Residential, Commercial, Testimonials, Gallery, About Us, Coupons, Contact Us

For the interior page, we're looking for the same inviting, informative and interactive feel to the site, preferably with a banner of some sort and the form close to the top of the page if not able to keep it above the fold in the banner. Page should also include sections with clients images used to avoid a wall of text.

Example Websites that the client likes:
https://www.brelkordairworks.example/
https://www.quellitemp.example/?ref=PzR8vLm2KqT4nW9sXe6YuJ3aBc
https://www.torvandclimate.example/nny/
https://www.wexlo.example/
https://otterbrookheat.example/

Industry/Entity Type

Hvac

Number of Pages Required

2 page

Requirements
Must have
• *Summarized from project description:
-financing image in prominent place
-content from development site
-images from clients folder
-button or "click here.." note in testimonials section
-form above the fold
Nice to have
-logo not on white background

```html
<!DOCTYPE html>
<html lang="en">
<head>
<meta charset="utf-8">
<title>Velmor Corp. — Residential &amp; Commercial HVAC</title>
<link href="https://fonts.googleapis.com/css2?family=Outfit:wght@400;500;600;700&family=Red+Hat+Display:wght@400;500;600;700&display=swap" rel="stylesheet">
<style>
:root{
  --red:#d9403a;
  --red-dark:#c4332e;
  --ink:#222429;
  --text:#55585e;
  --muted:#8a8d93;
  --line:#e4e4e6;
  --light:#f4f4f5;
  --white:#ffffff;
  --footer:#25272c;
  --footer-deep:#1d1f23;
  --orange:#f39a3b;
}
*{box-sizing:border-box;margin:0;padding:0}
html,body{width:1200px;height:4651px;overflow:hidden}
body{position:relative;font-family:"Red Hat Display",sans-serif;color:var(--text);background:var(--white)}
.abs{position:absolute}
h1,h2,h3,h4,.heading{font-family:"Outfit",sans-serif;color:var(--ink)}
.red{color:var(--red)}
.btn{position:absolute;display:flex;align-items:center;justify-content:center;gap:10px;font-family:"Outfit",sans-serif;font-size:10px;font-weight:600;letter-spacing:.4px;text-transform:uppercase;border-radius:3px;color:var(--white)}
.btn .dot{width:14px;height:14px;border-radius:50%;background:var(--white);display:flex;align-items:center;justify-content:center}
.btn-red{background:var(--red)}
.btn-dark{background:var(--ink)}
.btn-outline{border:1.5px solid var(--red);color:var(--red);background:transparent}
.btn-outline-white{border:1.5px solid var(--white);color:var(--white)}

/* header + hero */
.hero{position:absolute;left:0;top:0;width:1200px;height:614px;background:linear-gradient(100deg,#f3efe9 0%,#e9e2d8 35%,#cdbfae 60%,#a99a89 100%)}
.hero-photo{position:absolute;left:0;top:0;width:1200px;height:614px;background:radial-gradient(ellipse at 70% 45%,rgba(150,120,95,.45),transparent 60%),radial-gradient(ellipse at 8% 75%,rgba(90,130,60,.45),transparent 35%)}
.logo{position:absolute;left:162px;top:20px;display:flex;align-items:center;gap:10px}
.logo .mark{width:30px;height:30px;border-radius:50%;background:var(--ink)}
.logo .name{font-family:"Outfit",sans-serif;font-weight:700;font-size:36px;letter-spacing:3px;color:var(--ink)}
.call{position:absolute;left:626px;top:10px;display:flex;gap:10px;align-items:center}
.call small{display:block;font-size:11px;color:var(--ink)}
.call b{font-size:13px;color:var(--red);font-weight:600}
.badge-finance{position:absolute;left:922px;top:9px;width:116px;height:31px;background:var(--orange);border-radius:3px}
.nav{position:absolute;left:439px;top:68px;display:flex;gap:22px;font-family:"Outfit",sans-serif;font-size:12.5px;color:var(--ink)}
.nav .active{color:var(--red);border-bottom:1px solid var(--red)}
.hero-title{position:absolute;left:162px;top:214px}
.hero-title .t1{font-family:"Outfit",sans-serif;font-size:32px;font-weight:500;color:var(--ink);line-height:1}
.hero-title .t2{font-family:"Outfit",sans-serif;font-size:52px;font-weight:700;color:var(--red);line-height:1.1;margin-top:8px}
.hero-title .t3{font-size:18px;font-weight:500;color:var(--ink);margin-top:14px}

/* consultation */
.consult{position:absolute;left:0;top:614px;width:1200px;height:119px;background:var(--red)}
.consult h3{position:absolute;top:20px;width:100%;text-align:center;color:var(--white);font-size:20px;font-weight:500}
.field{position:absolute;top:61px;height:35px;background:var(--white);border-radius:2px;font-size:10px;color:var(--muted);padding:11px 12px}

/* about */
.about-text{position:absolute;left:224px;top:820px;width:320px}
.about-text h2{font-size:27px;font-weight:600;line-height:1.3}
.about-text p{font-size:12.5px;line-height:1.6;margin-top:14px}
.about-text p.small{font-size:11px;line-height:1.75}
.frame-corner{position:absolute;border-left:1.5px solid var(--line);border-top:1.5px solid var(--line)}
.photo{position:absolute}

/* services */
.services-bg{position:absolute;left:0;top:1155px;width:1200px;height:538px;background:linear-gradient(180deg,#fafafa,#eef0f2)}
.services-red{position:absolute;left:227px;top:1211px;width:378px;height:377px;background:var(--red)}
.svc-card{position:absolute;width:242px;height:173px;background:var(--white);text-align:center;padding-top:26px;box-shadow:0 2px 10px rgba(0,0,0,.04)}
.svc-card h4{font-size:12px;font-weight:600;margin-top:12px;text-transform:uppercase;letter-spacing:.3px}
.svc-card p{font-size:10px;line-height:1.7;margin:12px auto 0;width:180px}

/* solutions */
.center{position:absolute;left:0;width:1200px;text-align:center}
.sol-item{position:absolute;display:flex;gap:18px;width:240px}
.sol-item .ic{width:42px;height:42px;flex:none;border-left:1px solid var(--line);border-top:1px solid var(--line);display:flex;align-items:center;justify-content:center}
.sol-item h4{font-size:13px;font-weight:600;line-height:1.35}
.sol-item p{font-size:10px;line-height:1.6;margin-top:4px}

/* savings */
.sav-card{position:absolute;top:2834px;width:256px;height:244px;background:var(--white);padding:28px 26px;box-shadow:0 4px 18px rgba(0,0,0,.08)}
.sav-card h3{font-size:19px;font-weight:600;margin-top:12px}
.sav-card p{font-size:10.5px;line-height:1.65;margin-top:10px}
.sav-card .link{margin-top:20px;font-family:"Outfit",sans-serif;font-size:9.5px;font-weight:700;color:var(--red);text-transform:uppercase;display:flex;align-items:center;gap:8px}

/* footer */
.footer{position:absolute;left:0;top:4173px;width:1200px;height:478px;background:var(--footer);color:#b9bbc0}
.foot-col h5{font-family:"Outfit",sans-serif;font-size:11px;color:var(--white);font-weight:600;text-transform:uppercase;margin-bottom:14px}
.foot-col li{list-style:none;font-size:10px;line-height:20px}
.foot-contact{position:absolute;top:68px;display:flex;gap:14px;align-items:center;font-size:10px;line-height:1.5}
.ring{width:32px;height:32px;border-radius:50%;border:1.5px solid var(--red);display:flex;align-items:center;justify-content:center;flex:none}
.social{width:24px;height:24px;border-radius:50%;background:var(--red)}
</style>
</head>
<body>

<!-- HERO -->
<section class="hero">
  <div class="hero-photo" role="img" aria-label="Father lifting his daughter in the air in a bright living room with a green plant"></div>
  <div class="logo"><span class="mark"></span><span class="name">VELMOR</span></div>
  <div class="call">
    <svg width="18" height="18" viewBox="0 0 24 24" fill="none" stroke="#222429" stroke-width="2"><path d="M5 3h4l2 5-2.5 1.5a11 11 0 0 0 6 6L16 13l5 2v4a2 2 0 0 1-2 2A17 17 0 0 1 3 5a2 2 0 0 1 2-2z"/></svg>
    <div><small>Call Us</small><b>555 014-2290</b></div>
  </div>
  <a class="btn btn-red" style="left:773px;top:9px;width:146px;height:31px">Request Service <span class="dot"><svg width="8" height="8" viewBox="0 0 10 10"><path d="M2 5h6M5 2l3 3-3 3" stroke="#d9403a" stroke-width="1.6" fill="none"/></svg></span></a>
  <div class="badge-finance" role="img" aria-label="Financing badge"></div>
  <nav class="nav">
    <span class="active">Home</span><span>Residential</span><span>Commercial</span><span>Testimonials</span><span>Gallery</span><span>About Us</span><span>Coupons</span><span>Contact Us</span>
  </nav>
  <div class="hero-title">
    <div class="t1">YOUR COMFORT IS</div>
    <div class="t2">JUST A CALL AWAY</div>
    <div class="t3">Residential &amp; Commercial HVAC Solutions!</div>
  </div>
  <a class="btn btn-red" style="left:162px;top:381px;width:152px;height:34px">Heating Service <span class="dot"><svg width="8" height="8" viewBox="0 0 10 10"><path d="M2 5h6M5 2l3 3-3 3" stroke="#d9403a" stroke-width="1.6" fill="none"/></svg></span></a>
  <a class="btn btn-dark" style="left:327px;top:381px;width:151px;height:34px">Cooling Service <span class="dot"><svg width="8" height="8" viewBox="0 0 10 10"><path d="M2 5h6M5 2l3 3-3 3" stroke="#222429" stroke-width="1.6" fill="none"/></svg></span></a>
  <svg class="abs" style="left:594px;top:556px" width="12" height="22" viewBox="0 0 12 22"><path d="M6 0v20M1 15l5 5 5-5" stroke="#fff" stroke-width="1.4" fill="none"/></svg>
</section>

<!-- CONSULTATION -->
<section class="consult">
  <h3>CONTACT FREE CONSULTATION</h3>
  <div class="field" style="left:285px;width:152px">Name*</div>
  <div class="field" style="left:444px;width:152px">Phone*</div>
  <div class="field" style="left:603px;width:152px">Email*</div>
  <a class="btn btn-dark" style="left:763px;top:61px;width:150px;height:35px">Send Messsage <span class="dot"><svg width="8" height="8" viewBox="0 0 10 10"><path d="M2 5h6M5 2l3 3-3 3" stroke="#222429" stroke-width="1.6" fill="none"/></svg></span></a>
</section>

<!-- ABOUT -->
<section>
  <div class="frame-corner" style="left:204px;top:803px;width:40px;height:40px"></div>
  <div class="about-text">
    <h2>Local Brooklyn,<br>NY HVAC Contractors</h2>
    <p>Velmor Mechanical Air Duct, Insulation, Furnace, Air Conditioning repair and replacement company offers top repair services.</p>
    <p class="small">We can resolve any issues that may arise within your home. Our Brooklyn HVAC (heating, ventilating, and air conditioning) technicians are experts at inspecting and repairing systems that are not cooling or heating properly.</p>
  </div>
  <a class="btn btn-outline" style="left:224px;top:1069px;width:104px;height:32px;font-weight:500;text-transform:none;font-size:10.5px">Learn More</a>
  <div class="abs" style="left:610px;top:822px;width:365px;height:283px;background:var(--red)"></div>
  <div class="photo" style="left:596px;top:810px;width:367px;height:284px;background:linear-gradient(135deg,#dfe6ec,#a9b6c2 60%,#6d7b88)" role="img" aria-label="Technician checking an outdoor AC unit with red and blue pressure gauges"></div>
  <svg class="abs" style="left:612px;top:826px" width="335" height="252"><path d="M0 26V0h26M309 0h26v26M335 226v26h-26M26 252H0v-26" stroke="#fff" stroke-width="1.5" fill="none"/></svg>
</section>

<!-- SERVICES -->
<section>
  <div class="services-bg" role="img" aria-label="Faded white apartment buildings"></div>
  <div class="services-red"></div>
  <div class="abs" style="left:227px;top:1211px;width:256px;height:188px;background:linear-gradient(135deg,#e06a52,#c7453a)" role="img" aria-label="Smiling family at home, tinted red"></div>
  <h2 class="abs" style="left:258px;top:1244px;color:#fff;font-size:25px;font-weight:600">Services</h2>
  <p class="abs" style="left:258px;top:1293px;width:210px;color:#fff;font-size:10px;line-height:1.8">Well-functioning heating and A/C systems are imperative to your comfort, both in the office and at home.</p>

  <div class="svc-card" style="left:484px;top:1224px">
    <svg width="40" height="40" viewBox="0 0 40 40" fill="none" stroke="#222429" stroke-width="1.6"><circle cx="20" cy="20" r="15"/><path d="M20 5v30M5 20h30" stroke="#d9403a"/><circle cx="20" cy="20" r="4"/></svg>
    <h4>Air Conditioning</h4><p>Depend on us for timely, quality, and affordable air conditioning service.</p>
  </div>
  <div class="svc-card" style="left:727px;top:1224px">
    <svg width="40" height="40" viewBox="0 0 40 40" fill="none" stroke="#222429" stroke-width="1.6"><rect x="6" y="18" width="28" height="14" rx="2"/><path d="M12 22v6M18 22v6M24 22v6M30 22v6"/><path d="M14 6c-2 3 2 5 0 8M20 6c-2 3 2 5 0 8M26 6c-2 3 2 5 0 8" stroke="#d9403a"/></svg>
    <h4>Heating</h4><p>Depend on us for timely, quality, and affordable air conditioning service.</p>
  </div>
  <div class="svc-card" style="left:240px;top:1399px">
    <svg width="40" height="40" viewBox="0 0 40 40" fill="none" stroke="#222429" stroke-width="1.6"><path d="M8 32l14-14M26 6a7 7 0 0 0-6 9l-2 2 5 5 2-2a7 7 0 0 0 9-6l-4 3-4-4z"/><path d="M10 8l22 24" stroke="#d9403a"/></svg>
    <h4>Repairs</h4><p>Depend on us for timely, quality, and affordable air conditioning service.</p>
  </div>
  <div class="svc-card" style="left:484px;top:1399px">
    <svg width="40" height="40" viewBox="0 0 40 40" fill="none" stroke="#222429" stroke-width="1.6"><path d="M20 34V18l8-7 8 7v16z"/><rect x="25" y="25" width="6" height="9"/><circle cx="11" cy="12" r="4" stroke="#d9403a"/><path d="M4 34c0-6 3-10 7-10s6 3 7 6"/></svg>
    <h4>Serving Your Area</h4><p>Depend on us for timely, quality, and affordable air conditioning service.</p>
  </div>
  <div class="svc-card" style="left:727px;top:1399px">
    <svg width="40" height="40" viewBox="0 0 40 40" fill="none" stroke="#222429" stroke-width="1.6"><path d="M8 6h6l3 7-4 2a14 14 0 0 0 8 8l2-4 7 3v6a3 3 0 0 1-3 3A24 24 0 0 1 5 9a3 3 0 0 1 3-3z"/><text x="22" y="16" font-size="9" fill="#d9403a" stroke="none" font-family="Outfit">24</text><circle cx="27" cy="13" r="9" stroke="#d9403a" stroke-dasharray="3 2"/></svg>
    <h4>Support</h4><p>Depend on us for timely, quality, and affordable air conditioning service.</p>
  </div>
  <div class="abs" style="left:722px;top:1370px;width:3px;height:27px;background:var(--red)"></div>
  <div class="abs" style="left:700px;top:1394px;width:25px;height:3px;background:var(--red)"></div>
</section>

<!-- SOLUTIONS -->
<section>
  <div class="center heading" style="top:1764px;font-size:11px;font-weight:500;color:var(--ink)">SOLUTIONS</div>
  <h2 class="center" style="top:1784px;font-size:28px;font-weight:600">Trusted Home &amp; Commercial <span class="red">Solutions.</span></h2>
  <div class="center" style="top:1834px;font-size:12px">Serving both Residential &amp; Commercial Heating &amp; Air Conditioning Needs</div>

  <div class="sol-item" style="left:222px;top:1893px">
    <div class="ic"><svg width="26" height="26" viewBox="0 0 26 26" fill="none" stroke="#d9403a" stroke-width="1.4"><rect x="7" y="3" width="8" height="20" rx="2"/><path d="M18 8h5M18 13h5M18 18h5" stroke="#222429"/></svg></div>
    <div><h4>Air Purifier System</h4><p>Lorem Ipsum is simply dummy text of the printing.</p></div>
  </div>
  <div class="sol-item" style="left:478px;top:1893px">
    <div class="ic"><svg width="26" height="26" viewBox="0 0 26 26" fill="none" stroke="#222429" stroke-width="1.4"><circle cx="13" cy="13" r="10"/><circle cx="13" cy="13" r="5" stroke="#d9403a"/></svg></div>
    <div><h4>HVAC Maintenance<br>Tune Up and Inspection</h4><p>Lorem Ipsum is simply dummy text of the printing.</p></div>
  </div>
  <div class="sol-item" style="left:743px;top:1893px">
    <div class="ic"><svg width="26" height="26" viewBox="0 0 26 26" fill="none" stroke="#222429" stroke-width="1.4"><path d="M4 22L16 10M18 3a5 5 0 0 0-4 6l5 5a5 5 0 0 0 6-4l-3 2-3-3z"/><path d="M5 4l17 18" stroke="#d9403a"/></svg></div>
    <div><h4>HVAC Parts, Repair,<br>Installation</h4><p>Lorem Ipsum is simply dummy text of the printing.</p></div>
  </div>
  <div class="sol-item" style="left:222px;top:2003px">
    <div class="ic"><svg width="26" height="26" viewBox="0 0 26 26" fill="none" stroke="#222429" stroke-width="1.4"><path d="M5 12a8 8 0 0 1 14-5l2-2v6h-6l2-2a5 5 0 0 0-9 3"/><path d="M21 14a8 8 0 0 1-14 5l-2 2v-6h6l-2 2a5 5 0 0 0 9-3" stroke="#d9403a"/></svg></div>
    <div><h4>HVAC Replacement<br>Cost and Installation</h4><p>Lorem Ipsum is simply dummy text of the printing.</p></div>
  </div>
  <div class="sol-item" style="left:478px;top:2003px">
    <div class="ic"><svg width="28" height="26" viewBox="0 0 28 26" fill="none" stroke="#222429" stroke-width="1.4"><rect x="2" y="8" width="24" height="8" rx="1"/><path d="M5 19h18" stroke="#d9403a"/></svg></div>
    <div><h4>Ductless Systems</h4><p>Lorem Ipsum is simply dummy text of the printing.</p></div>
  </div>
  <div class="sol-item" style="left:743px;top:2003px">
    <div class="ic"><svg width="26" height="26" viewBox="0 0 26 26" fill="none" stroke="#222429" stroke-width="1.4"><rect x="4" y="3" width="18" height="20"/><path d="M4 9h18"/><path d="M9 14v5M13 14v5M17 14v5" stroke="#d9403a"/></svg></div>
    <div><h4>Gas Furnace Installations</h4><p>Lorem Ipsum is simply dummy text of the printing.</p></div>
  </div>

  <div class="abs" style="left:235px;top:2106px;width:730px;height:1px;background:var(--line)"></div>
  <div class="abs" style="left:714px;top:2130px;width:1px;height:65px;background:var(--line)"></div>
  <p class="abs" style="left:242px;top:2130px;width:420px;font-size:11px;line-height:1.85">Velmor Mechanical Contractors Corp Is Here To Make You Smile With Professional HVAC Services</p>
  <p class="abs red" style="left:242px;top:2184px;font-size:11.5px">Please Call To Confirm Service In Your Area</p>
  <a class="btn btn-red" style="left:783px;top:2142px;width:158px;height:35px">Get Started Now <span class="dot"><svg width="8" height="8" viewBox="0 0 10 10"><path d="M2 5h6M5 2l3 3-3 3" stroke="#d9403a" stroke-width="1.6" fill="none"/></svg></span></a>
</section>

<!-- EXPERIENCE -->
<section>
  <div class="abs" style="left:0;top:2240px;width:1200px;height:440px;background:linear-gradient(160deg,#fbfbfb,#f1f1f2)"></div>
  <h2 class="abs" style="left:273px;top:2360px;font-size:31px;font-weight:600;line-height:1.15">We’re Backed<br>by 20 Years of<br><span class="red">Experience.</span></h2>
  <div class="photo" style="left:606px;top:2283px;width:369px;height:287px;background:linear-gradient(180deg,#eceae6 0%,#dad6d0 55%,#9c9a96 100%)" role="img" aria-label="Woman relaxing on a grey sofa beneath a wall-mounted AC unit"></div>
  <div class="abs" style="left:760px;top:2398px;width:60px;height:60px;border-radius:50%;background:#fff;display:flex;align-items:center;justify-content:center"><svg width="12" height="12" viewBox="0 0 12 12"><path d="M3 1l8 5-8 5z" fill="#2f6fd6"/></svg></div>
</section>

<!-- SAVINGS -->
<section>
  <h2 class="center" style="top:2750px;font-size:30px;font-weight:600">SAVINGS CENTER</h2>
  <div class="abs" style="left:569px;top:2796px;width:62px;height:2px;background:var(--red)"></div>
  <div class="abs" style="left:0;top:2834px;width:1200px;height:532px;background:linear-gradient(180deg,#ece6de 0%,#d9cfc3 45%,#a99b8b 80%,#8e7f6f 100%)" role="img" aria-label="Happy family lying together on a living room floor"></div>

  <div class="sav-card" style="left:197px">
    <svg width="64" height="50" viewBox="0 0 64 50" fill="none" stroke="#222429" stroke-width="1.8"><rect x="2" y="2" width="40" height="30"/><path d="M10 40l24-24M30 10l12 12" /><path d="M44 30l14 14M40 42h20" stroke="#d9403a"/></svg>
    <h3>Maint Plan</h3>
    <p>Lorem ipsum dolor sit amet, consectetur adipiscing elit. Sed turpis neque, porta sed nisl ut, consequat venenatis..</p>
    <div class="link">Maintenance Plan <svg width="14" height="14" viewBox="0 0 14 14"><circle cx="7" cy="7" r="7" fill="#d9403a"/><path d="M4 7h6M7.5 4.5L10 7l-2.5 2.5" stroke="#fff" stroke-width="1.4" fill="none"/></svg></div>
  </div>
  <div class="sav-card" style="left:471px">
    <svg width="64" height="50" viewBox="0 0 64 50" fill="none" stroke="#222429" stroke-width="1.8"><circle cx="32" cy="14" r="11" fill="#d9403a" stroke="none"/><text x="28" y="19" font-size="13" fill="#fff" stroke="none" font-family="Outfit">$</text><path d="M6 36c10-6 18-4 26 0s18 2 28-4" /><path d="M6 44c10-4 20-2 30 0" /></svg>
    <h3>Financing</h3>
    <p>Lorem ipsum dolor sit amet, consectetur adipiscing elit. Sed turpis neque, porta sed nisl ut, consequat venenatis..</p>
    <div class="link">Apply for Financing <svg width="14" height="14" viewBox="0 0 14 14"><circle cx="7" cy="7" r="7" fill="#d9403a"/><path d="M4 7h6M7.5 4.5L10 7l-2.5 2.5" stroke="#fff" stroke-width="1.4" fill="none"/></svg></div>
  </div>
  <div class="sav-card" style="left:745px">
    <svg width="64" height="50" viewBox="0 0 64 50" fill="none" stroke="#222429" stroke-width="1.8"><rect x="6" y="12" width="48" height="30"/><rect x="14" y="18" width="30" height="16" stroke="#d9403a"/><text x="23" y="31" font-size="12" fill="#222429" stroke="none" font-family="Outfit">%</text><path d="M2 8h6M5 5v6" stroke="#d9403a"/></svg>
    <h3>Promotions</h3>
    <p>Lorem ipsum dolor sit amet, consectetur adipiscing elit. Sed turpis neque, porta sed nisl ut, consequat venenatis..</p>
    <div class="link">View All Coupons <svg width="14" height="14" viewBox="0 0 14 14"><circle cx="7" cy="7" r="7" fill="#d9403a"/><path d="M4 7h6M7.5 4.5L10 7l-2.5 2.5" stroke="#fff" stroke-width="1.4" fill="none"/></svg></div>
  </div>
</section>

<!-- TESTIMONIALS -->
<section>
  <div class="abs" style="left:0;top:3366px;width:1200px;height:443px;background:linear-gradient(180deg,#d9463f,#cf3d37)" role="img" aria-label="Red-tinted living room background"></div>
  <div class="center heading" style="top:3425px;font-size:11px;font-weight:500;color:#fff">TESTIMONIALS</div>
  <h2 class="center" style="top:3450px;font-size:31px;font-weight:600;color:#fff">Our Happy Customers Say</h2>
  <p class="abs" style="left:306px;top:3536px;width:588px;text-align:center;color:#fff;font-size:13.5px;line-height:1.8">Thank you so much for doing such a wonderful job on our air conditioning unit. I am very happy with the service provided to me from Velmor Mechanical Contractors. The staff gathers my information before helping me out to see what they could do for me. I am thankful for all of your help and services.</p>
  <div class="center" style="top:3646px;color:#fff;font-size:13px">- Daniel M.</div>
  <a class="btn btn-outline-white" style="left:552px;top:3697px;width:127px;height:36px;font-weight:500">Click Here <span class="dot"><svg width="8" height="8" viewBox="0 0 10 10"><path d="M2 5h6M5 2l3 3-3 3" stroke="#d9403a" stroke-width="1.6" fill="none"/></svg></span></a>
  <div class="abs" style="left:212px;top:3552px;width:30px;height:30px;border-radius:50%;background:rgba(255,255,255,.35);display:flex;align-items:center;justify-content:center"><svg width="14" height="14" viewBox="0 0 14 14"><path d="M12 7H2M6 3L2 7l4 4" stroke="#d9403a" stroke-width="1.8" fill="none"/></svg></div>
  <div class="abs" style="left:956px;top:3552px;width:30px;height:30px;border-radius:50%;background:#fff;display:flex;align-items:center;justify-content:center"><svg width="14" height="14" viewBox="0 0 14 14"><path d="M2 7h10M8 3l4 4-4 4" stroke="#d9403a" stroke-width="1.8" fill="none"/></svg></div>
</section>

<!-- SCHEDULE -->
<section>
  <h2 class="center" style="top:3874px;font-size:28px;font-weight:400;line-height:1.35">To schedule an appointment with our furnace and <b style="font-weight:600">air<br>conditioning repair and installation experts.</b></h2>
  <div class="center" style="top:3962px;font-size:13px">We will be in touch with you to verify your appointment.</div>
  <div class="abs" style="left:307px;top:4028px;display:flex;gap:16px;align-items:center">
    <div style="width:42px;height:42px;border-radius:50%;background:var(--red);display:flex;align-items:center;justify-content:center"><svg width="18" height="18" viewBox="0 0 24 24" fill="none" stroke="#fff" stroke-width="2.2"><path d="M5 3h4l2 5-2.5 1.5a11 11 0 0 0 6 6L16 13l5 2v4a2 2 0 0 1-2 2A17 17 0 0 1 3 5a2 2 0 0 1 2-2z"/></svg></div>
    <div><div class="heading" style="font-size:10.5px;font-weight:600">NEED HELP NOW?</div><div class="heading red" style="font-size:22px;font-weight:500">CALL: <b style="font-weight:700">555 014-2290</b></div></div>
  </div>
  <div class="abs" style="left:612px;top:4022px;width:1px;height:55px;background:var(--line)"></div>
  <a class="btn btn-red" style="left:661px;top:4033px;width:160px;height:36px">Request Service <span class="dot"><svg width="8" height="8" viewBox="0 0 10 10"><path d="M2 5h6M5 2l3 3-3 3" stroke="#d9403a" stroke-width="1.6" fill="none"/></svg></span></a>
</section>

<!-- FOOTER -->
<footer class="footer">
  <div class="foot-contact" style="left:236px">
    <div class="ring"><svg width="12" height="14" viewBox="0 0 12 14" fill="none" stroke="#d9403a" stroke-width="1.4"><path d="M6 13s5-4.5 5-8A5 5 0 0 0 1 5c0 3.5 5 8 5 8z"/><circle cx="6" cy="5" r="1.7"/></svg></div>
    <div>Harlow's, 543 Lorem, Ipsum<br>simply dummy text of the printing<br>and typesetting.</div>
  </div>
  <div class="foot-contact" style="left:530px">
    <div class="ring"><svg width="12" height="14" viewBox="0 0 12 14" fill="none" stroke="#d9403a" stroke-width="1.4"><path d="M6 13s5-4.5 5-8A5 5 0 0 0 1 5c0 3.5 5 8 5 8z"/><circle cx="6" cy="5" r="1.7"/></svg></div>
    <div><span style="color:#fff">Phone</span><br>555 014-2290</div>
  </div>
  <div class="foot-contact" style="left:802px">
    <div class="ring"><svg width="12" height="14" viewBox="0 0 12 14" fill="none" stroke="#d9403a" stroke-width="1.4"><path d="M6 13s5-4.5 5-8A5 5 0 0 0 1 5c0 3.5 5 8 5 8z"/><circle cx="6" cy="5" r="1.7"/></svg></div>
    <div><span style="color:#fff">Email</span><br>office@velmorcorp.example</div>
  </div>
  <div class="abs" style="left:228px;top:140px;width:744px;height:1px;background:rgba(255,255,255,.1)"></div>

  <div class="abs" style="left:234px;top:190px;display:flex;align-items:center;gap:10px">
    <span style="width:30px;height:30px;border-radius:50%;background:#fff"></span>
    <span style="font-family:Outfit,sans-serif;font-weight:700;font-size:36px;letter-spacing:3px;color:#fff">VELMOR</span>
  </div>
  <p class="abs" style="left:234px;top:302px;width:220px;font-size:10px;line-height:1.9">Lorem Ipsum is simply dummy text of the printing and typesetting industry. Lorem Ipsum has been the industry's.</p>

  <div class="foot-col abs" style="left:534px;top:186px"><h5>Links</h5><ul><li>Home</li><li>Residential</li><li>Commercial</li><li>Testimonials</li><li>Gallery</li><li>About Us</li><li>Coupons</li></ul></div>
  <div class="foot-col abs" style="left:682px;top:186px"><h5>Air Conditioning</h5><ul><li>AC Repair</li><li>AC Installation</li><li>AC Service</li><li>Ductless Air Conditioning</li></ul></div>
  <div class="foot-col abs" style="left:868px;top:186px"><h5>Heating</h5><ul><li>Furnace Repair</li><li>Furnace Installation</li><li>Furnace Service</li><li>Contact Us</li></ul></div>
  <div class="heading abs" style="left:718px;top:336px;font-size:11px;font-weight:600;color:#fff">SOCIAL</div>
  <div class="abs" style="left:847px;top:329px;display:flex;gap:8px"><span class="social"></span><span class="social"></span><span class="social"></span><span class="social"></span></div>

  <div class="abs" style="left:0;top:412px;width:1200px;height:66px;background:var(--footer-deep)"></div>
  <div class="abs" style="left:234px;top:431px;font-size:10px">© 2021 <span class="red">velmorcorp.example</span>. All Rights Reserved.</div>
  <div class="abs" style="left:814px;top:431px;font-size:10px">Privacy Policy &nbsp;&nbsp;|&nbsp;&nbsp; Terms of Use</div>
</footer>

<!-- service van overlapping schedule and footer -->
<div class="abs" style="left:830px;top:4016px;width:370px;height:200px;background:linear-gradient(180deg,#fafafa,#dcdcdc);border-radius:60px 10px 20px 20px" role="img" aria-label="White company service van"></div>

</body>
</html>
```